Whitby's Meadow Larder Limited (Uncoded design only)

To design a new modern website to replace an existing website.
www.tolmerpies.co.uk
we want to keep the same website address and pages - unless you hae new ideas for the pages.
We are initially looking for design only (no coding requirements)
We want wording 'Whitby's Crust Bakes' to be used and Whitby's Meadow Larder Limited to be the comapny address rather than what it is now.
I attach a new logo 'Whitby lad' and new packaing design (Zip file). NOTE the blue man is to be replaced with the new 'Whitbys lad 'file i.e.the man with the union jack flag on his chest.
We would like coordination of the packing colourson the new website please.

Target Market(s)

Online sales to supermarkets

Industry/Entity Type

Food manufacturing

Coding

Coded - Design and coding required

Number of Pages Required

4 page

Font styles to use
Other font styles liked:
• Happy for any choice of font styles as I'm not stuck with the font of the packaging. I'm happy to go with what you feel looks the best and we can change the package to suit

Requirements
Must have
• Links to Facebook, Instagram and LinkedIn

```html
<!DOCTYPE html>
<html lang="en">
<head>
<meta charset="utf-8">
<title>Whitby's Crust Bakes</title>
<link rel="stylesheet" href="https://fonts.googleapis.com/css2?family=Oswald:wght@400;500;600&family=Poppins:wght@400;500;600;700&display=swap">
<style>
:root{
  --red:#e1141d;
  --navy:#0b1f8c;
  --navy-deep:#081870;
  --navy-field:#1a2f9c;
  --ink:#141414;
  --grey-text:#444;
  --pale:#e6e7ee;
  --pink:#f6d0d5;
  --white:#fff;
}
*{margin:0;padding:0;box-sizing:border-box}
html,body{width:1200px;height:4474px;overflow:hidden}
body{position:relative;background:var(--white);font-family:'Poppins',sans-serif;color:var(--ink)}
.abs{position:absolute}
.backdrop{position:absolute;left:0;top:0;width:1200px;height:4474px}
.heading{font-family:'Oswald',sans-serif;font-weight:500;text-transform:uppercase;line-height:1.05;color:var(--ink)}
.lead{font-family:'Oswald',sans-serif;font-weight:400;text-transform:uppercase;color:var(--grey-text)}
.btn{position:absolute;display:flex;align-items:center;justify-content:center;background:var(--red);color:var(--white);font-weight:700;font-size:15px;text-transform:uppercase;text-decoration:none;letter-spacing:.3px}
.photo{position:absolute}

/* nav */
.site-nav{position:absolute;left:0;top:0;width:1200px;height:80px;background:var(--white)}
.site-nav ul{position:absolute;right:158px;top:34px;display:flex;gap:28px;list-style:none}
.site-nav a{font-size:13px;font-weight:600;color:var(--ink);text-decoration:none;text-transform:uppercase}
.site-nav a.current{color:var(--red)}
.cart{position:absolute;left:1067px;top:21px;width:44px;height:44px;border-radius:50%;background:var(--ink);display:flex;align-items:center;justify-content:center}
.brand{position:absolute;left:80px;top:-9px;width:174px;height:174px;border-radius:50%;background:var(--white);display:flex;align-items:center;justify-content:center;text-align:center;font-weight:700;font-size:17px;line-height:1.25;color:var(--ink);z-index:3}

/* hero */
.hero-title{left:88px;top:282px;font-family:'Oswald',sans-serif;font-weight:600;font-size:76px;line-height:1;color:var(--white);text-transform:uppercase}
.hero-title em{font-style:normal;color:var(--red)}
.hero-sub{left:88px;top:448px;font-family:'Oswald',sans-serif;font-size:23px;color:var(--white);text-transform:uppercase}
.hero-bar{left:52px;top:288px;width:12px;height:265px;background:#3b3b44}

/* cooking cards */
.cook-card{position:absolute;top:1921px;width:200px;height:268px;background:var(--white);text-align:center;box-shadow:0 4px 14px rgba(0,0,0,.18)}
.cook-card svg{margin-top:30px}
.cook-card h3{font-family:'Oswald',sans-serif;font-weight:500;font-size:17px;margin-top:14px;text-transform:uppercase}
.cook-card p{font-size:11px;line-height:18px;color:var(--grey-text);margin:10px 22px 0}

/* products */
.product{position:absolute;top:2915px;width:242px;height:320px;background:var(--white);box-shadow:0 4px 14px rgba(0,0,0,.12);text-align:center}
.product .photo{position:static;width:242px;height:242px}
.product h4{font-family:'Oswald',sans-serif;font-weight:500;font-size:11px;margin-top:22px;text-transform:uppercase}
.product .price{font-weight:700;color:var(--red);font-size:16px;margin-top:2px}
.pager{position:absolute;top:3269px;width:49px;height:49px;display:flex;align-items:center;justify-content:center}

/* banner */
.apprentice{left:109px;top:3828px;width:980px;height:179px;background:var(--red);z-index:2}
.apprentice h2{position:absolute;left:99px;top:60px;font-family:'Oswald',sans-serif;font-weight:500;font-size:44px;color:var(--white);text-transform:uppercase}
.apprentice .btn{left:709px;top:66px;width:172px;height:45px;background:var(--white);color:var(--ink)}

/* footer */
.foot-col h5{font-family:'Oswald',sans-serif;font-weight:600;font-size:17px;color:var(--white);text-transform:uppercase}
.foot-col ul{list-style:none;margin-top:16px}
.foot-col li{font-size:11px;line-height:27px;color:var(--white)}
.field{position:absolute;background:var(--navy-field);border:1px solid #3247b0;color:#c8cdf0;font-size:11px;padding:8px 12px}
.social{position:absolute;top:4223px;width:44px;height:44px;border-radius:50%;border:1.5px solid rgba(255,255,255,.5)}
.copyright{left:0;top:4417px;width:1200px;height:57px;background:var(--navy-deep);color:var(--white);font-size:11px;font-weight:600;display:flex;align-items:center;justify-content:center;text-transform:uppercase}
.chat{left:1129px;top:4398px;width:46px;height:46px;border-radius:50%;background:var(--red);display:flex;align-items:center;justify-content:center}
</style>
</head>
<body>

<svg class="backdrop" width="1200" height="4474" viewBox="0 0 1200 4474" aria-hidden="true">
  <defs>
    <linearGradient id="heroShade" x1="0" y1="0" x2="0" y2="1">
      <stop offset="0" stop-color="#0a0a0c"/>
      <stop offset=".55" stop-color="#15151c"/>
      <stop offset="1" stop-color="#55556f"/>
    </linearGradient>
  </defs>
  <rect x="0" y="80" width="1200" height="820" fill="url(#heroShade)"/>
  <rect x="0" y="1754" width="1200" height="420" fill="var(--navy)"/>
  <polygon points="0,2174 1200,2174 1200,2171 0,2371" fill="var(--navy)"/>
  <polygon points="0,2371 1200,2171 1200,2190 0,2425" fill="var(--pale)"/>
  <polygon points="903,2605 1200,2362 1200,2901" fill="var(--pink)"/>
  <polygon points="0,3850 1200,3782 1200,3800 0,3872" fill="var(--pale)"/>
  <polygon points="0,3872 1200,3800 1200,4474 0,4474" fill="var(--navy)"/>
</svg>

<nav class="site-nav">
  <ul>
    <li><a class="current" href="#">Home</a></li>
    <li><a href="#">Privacy Policy</a></li>
    <li><a href="#">Contact</a></li>
    <li><a href="#">Shop</a></li>
    <li><a href="#">Delivery</a></li>
  </ul>
  <div class="cart">
    <svg width="22" height="20" viewBox="0 0 22 20" fill="none" stroke="#fff" stroke-width="1.6"><path d="M1 2h3l3 11h11l2-8H6"/><circle cx="8.5" cy="17" r="1.4"/><circle cx="16.5" cy="17" r="1.4"/></svg>
  </div>
</nav>
<div class="brand">Whitby's<br>Crust Bakes</div>

<!-- hero -->
<div class="photo" role="img" aria-label="Rag pudding with chips, peas, tomato and pickled red cabbage on a white plate" style="left:460px;top:110px;width:740px;height:760px;background:radial-gradient(ellipse at 55% 55%,#d9c48e 0%,#b7934d 28%,#5d6b2a 48%,rgba(30,30,36,0) 72%)"></div>
<svg class="backdrop" width="1200" height="4474" viewBox="0 0 1200 4474" aria-hidden="true" style="pointer-events:none">
  <polygon points="0,686 1200,886 1200,960 0,960" fill="#fff"/>
  <polygon points="900,836 1200,886 1200,945" fill="var(--pale)"/>
</svg>
<div class="abs hero-bar"></div>
<h1 class="abs hero-title"><em>Handmade</em> in<br>Lancashire</h1>
<p class="abs hero-sub">Local apprentice opportunity</p>
<a class="btn" href="#" style="left:88px;top:502px;width:172px;height:47px">Apply here</a>

<!-- rag puddings -->
<div class="photo" role="img" aria-label="Decorative striped block" style="left:177px;top:1141px;width:209px;height:209px;background:#2b3a98"></div>
<div class="photo" role="img" aria-label="Rice, nachos and salad served in white dishes" style="left:200px;top:877px;width:360px;height:450px;background:linear-gradient(160deg,#2e2f2a 0%,#c9b45a 30%,#ecebe3 60%,#1c1c1c 100%)"></div>
<h2 class="abs heading" style="left:634px;top:1000px;font-size:42px">Our rag puddings</h2>
<p class="abs lead" style="left:634px;top:1056px;width:420px;font-size:21px;line-height:27px;color:var(--ink)">Are made from suet pastry and the very<br>best cuts of beefsteak without the use<br>of any preservatives.</p>
<a class="btn" href="#" style="left:634px;top:1162px;width:172px;height:45px">Buy online</a>

<!-- historically -->
<h2 class="abs heading" style="left:170px;top:1445px;font-size:42px">Historically,<br>the puddings</h2>
<p class="abs lead" style="left:170px;top:1548px;width:340px;font-size:17px;line-height:24px">Take their name from the cloth they are<br>wrapped in while they are steamed.<br>Today, a hi-tech material is used instead<br>of the original ‘rags’.</p>
<div class="photo" role="img" aria-label="Grilled steak with roasted squash and salad leaves on a dark plate" style="left:564px;top:1303px;width:476px;height:476px;border-radius:50%;background:radial-gradient(circle at 45% 50%,#7a3b22 0%,#4a3a20 35%,#1d1d1d 62%,#0f0f0f 100%);box-shadow:0 18px 30px rgba(0,0,0,.25)"></div>

<!-- how do you like yours -->
<h2 class="abs heading" style="left:0;top:1848px;width:1200px;text-align:center;font-size:40px;color:var(--white)">How do you like yours?</h2>
<div class="cook-card" style="left:182px">
  <svg width="70" height="78" viewBox="0 0 70 78" fill="none" stroke="#111" stroke-width="2.5"><rect x="3" y="3" width="64" height="72" rx="3"/><line x1="3" y1="18" x2="67" y2="18"/><circle cx="14" cy="10.5" r="2.5" fill="#e1141d" stroke="none"/><circle cx="24" cy="10.5" r="2.5" fill="#e1141d" stroke="none"/><rect x="12" y="28" width="46" height="38"/><path d="M22 56h26M26 56a9 9 0 0 1 18 0M35 44v3" stroke="#e1141d"/></svg>
  <h3>Oven bake</h3>
  <p>Aenean sollicitudin lorem quis bibendum auctor nisi elit consequat...</p>
</div>
<div class="cook-card" style="left:394px">
  <svg width="80" height="78" viewBox="0 0 80 78" fill="none" stroke="#111" stroke-width="2.5"><path d="M32 4c-3 4 3 7 0 11M40 4c-3 4 3 7 0 11M48 4c-3 4 3 7 0 11"/><path d="M16 24h48M20 24v24h40V24" stroke="#e1141d"/><rect x="6" y="54" width="68" height="18"/><circle cx="24" cy="63" r="2.5"/><circle cx="40" cy="63" r="2.5"/><circle cx="56" cy="63" r="2.5"/></svg>
  <h3>Steam</h3>
  <p>Aenean sollicitudin lorem quis bibendum auctor nisi elit consequat...</p>
</div>
<div class="cook-card" style="left:606px">
  <svg width="90" height="78" viewBox="0 0 90 78" fill="none" stroke="#111" stroke-width="2.5"><rect x="3" y="6" width="84" height="66" rx="3"/><rect x="11" y="15" width="54" height="48"/><line x1="74" y1="15" x2="80" y2="15"/><circle cx="77" cy="38" r="4"/><circle cx="77" cy="52" r="4"/><path d="M24 50h28M27 50a11 11 0 0 0 22 0" stroke="#e1141d"/><path d="M32 26c-2 3 2 5 0 8M38 26c-2 3 2 5 0 8M44 26c-2 3 2 5 0 8"/></svg>
  <h3>Microwave</h3>
  <p>Aenean sollicitudin lorem quis bibendum auctor nisi elit consequat...</p>
</div>
<div class="cook-card" style="left:818px">
  <svg width="84" height="78" viewBox="0 0 84 78" fill="none" stroke="#111" stroke-width="2.5"><path d="M34 4c-3 4 3 7 0 11M42 4c-3 4 3 7 0 11M50 4c-3 4 3 7 0 11"/><path d="M4 28h76M10 28v40h64V28M10 36H4M74 36h6"/><circle cx="30" cy="46" r="3" fill="#e1141d" stroke="none"/><circle cx="52" cy="46" r="3" fill="#e1141d" stroke="none"/><circle cx="41" cy="58" r="3" fill="#e1141d" stroke="none"/></svg>
  <h3>Boil in the bag</h3>
  <p>Aenean sollicitudin lorem quis bibendum auctor nisi elit consequat...</p>
</div>

<!-- sweet or savoury -->
<div class="photo" role="img" aria-label="Grilled steak and vegetables in a skillet on a wooden board with a fork" style="left:260px;top:2249px;width:322px;height:452px;background:linear-gradient(170deg,#7a4428 0%,#3b1f14 40%,#6b3a24 70%,#8a5534 100%);border-radius:10px"></div>
<h2 class="abs heading" style="left:618px;top:2398px;font-size:42px">Sweet or savoury</h2>
<p class="abs lead" style="left:618px;top:2450px;font-size:17px">Try our apple rag puddings</p>
<a class="btn" href="#" style="left:622px;top:2494px;width:172px;height:45px">Buy online</a>

<!-- delivery -->
<h2 class="abs heading" style="left:0;top:2762px;width:1200px;text-align:center;font-size:42px;line-height:46px">Local delivery only £1 in<br>all ‘OL’ postcodes</h2>
<p class="abs lead" style="left:0;top:2862px;width:1200px;text-align:center;font-size:13px">Delivery charge will be applied automatically when you proceed to checkout as local postcode is recognised.</p>
<div class="product" style="left:97px">
  <div class="photo" role="img" aria-label="Meat and potato pie with chips, peas, salad and red cabbage" style="background:linear-gradient(150deg,#3a3a30,#d8c58a 45%,#e8e8e0 65%,#3b7a2a)"></div>
  <h4>Meat and potato pie – for 2 people</h4><div class="price">£4.60</div>
</div>
<div class="product" style="left:352px">
  <div class="photo" role="img" aria-label="Rag puddings with chips on a white plate" style="background:linear-gradient(150deg,#1a1a1a,#e5cc78 45%,#efe9d8 65%,#5b3420)"></div>
  <h4>Rag puddings 8 pack</h4><div class="price">£12.80</div>
</div>
<div class="product" style="left:607px">
  <div class="photo" role="img" aria-label="Traditional beef chilli with rice and nachos" style="background:linear-gradient(150deg,#2a2a24,#d6b85a 40%,#eeeee6 65%,#8a4a22)"></div>
  <h4>Traditional beef chilli</h4><div class="price">£2.50</div>
</div>
<div class="product" style="left:861px">
  <div class="photo" role="img" aria-label="Family size meat and potato pie with peas and carrots" style="background:linear-gradient(150deg,#3a3530,#c7a468 45%,#d9c9a4 70%,#6a5a48)"></div>
  <h4>Meat and potato pie – family size</h4><div class="price">£6.70</div>
</div>
<div class="pager" style="left:545px;background:#ddd"><svg width="10" height="14" viewBox="0 0 10 14" fill="none" stroke="#111" stroke-width="2"><path d="M7 2L2 7l5 5"/></svg></div>
<div class="pager" style="left:604px;background:var(--ink)"><svg width="10" height="14" viewBox="0 0 10 14" fill="none" stroke="#fff" stroke-width="2"><path d="M3 2l5 5-5 5"/></svg></div>

<!-- purpose -->
<h2 class="abs heading" style="left:214px;top:3416px;font-size:42px;line-height:45px">Our purpose<br>built facilities</h2>
<p class="abs lead" style="left:214px;top:3522px;width:400px;font-size:16px;line-height:22px">Are dedicated to providing consistantly perfect<br>rag puddings to customers worldwide</p>
<div class="photo" role="img" aria-label="Whitby lad mascot illustration" style="left:243px;top:3578px;width:287px;height:252px;background:radial-gradient(ellipse at 50% 60%,#d8dbe8 0%,#eef0f5 55%,rgba(255,255,255,0) 75%)"></div>
<div class="photo" role="img" aria-label="Production line workers in the kitchen" style="left:632px;top:3405px;width:168px;height:168px;background:linear-gradient(160deg,#9aa4b8,#5e6e8e)"></div>
<div class="photo" role="img" aria-label="Industrial mixing machine" style="left:807px;top:3405px;width:168px;height:168px;background:linear-gradient(160deg,#c4c8d0,#7e8796)"></div>
<div class="photo" role="img" aria-label="Staff preparing puddings by hand" style="left:632px;top:3580px;width:168px;height:168px;background:linear-gradient(160deg,#5b74b8,#2a3f78)"></div>
<div class="photo" role="img" aria-label="Worker operating steaming equipment" style="left:807px;top:3580px;width:168px;height:168px;background:linear-gradient(160deg,#8c98b0,#46597e)"></div>

<!-- apprentice banner -->
<div class="abs apprentice">
  <h2>Local apprentice opportunity</h2>
  <a class="btn" href="#">Apply here</a>
</div>

<!-- footer -->
<div class="abs foot-col" style="left:90px;top:4110px">
  <h5>Quick links</h5>
  <ul><li>Home</li><li>Privacy Policy</li><li>Contact Us</li><li>Shop</li><li>Delivery</li></ul>
</div>
<div class="abs foot-col" style="left:233px;top:4110px">
  <h5>What we do</h5>
  <ul><li>Oven Bake</li><li>Steam</li><li>Microwave</li><li>Boil in the bag</li></ul>
</div>
<div class="abs foot-col" style="left:396px;top:4110px">
  <h5>Contact us</h5>
  <ul><li>Please contact us via this form and we will get back to soon</li></ul>
</div>
<div class="field" style="left:400px;top:4183px;width:148px;height:31px">Name</div>
<div class="field" style="left:556px;top:4183px;width:146px;height:31px">Email</div>
<div class="field" style="left:710px;top:4183px;width:145px;height:31px">Subject</div>
<div class="field" style="left:400px;top:4224px;width:455px;height:90px">Message</div>
<a class="btn" href="#" style="left:400px;top:4330px;width:106px;height:37px;font-size:13px">Submit</a>
<div class="social" style="left:907px" role="img" aria-label="Social profile link 1"></div>
<div class="social" style="left:961px" role="img" aria-label="Social profile link 2"></div>
<div class="social" style="left:1015px" role="img" aria-label="Social profile link 3"></div>
<div class="social" style="left:1069px" role="img" aria-label="Social profile link 4"></div>

<div class="abs copyright">© 2023 Whitby's Crust Bakes all rights reserved.</div>
<div class="abs chat">
  <svg width="24" height="22" viewBox="0 0 24 22" fill="#fff"><path d="M12 2C6 2 2 5.6 2 10c0 2.4 1.2 4.5 3.2 6L4 20l4.6-2.4c1 .3 2.2.4 3.4.4 6 0 10-3.6 10-8S18 2 12 2z"/><circle cx="8" cy="10" r="1.3" fill="#e1141d"/><circle cx="12" cy="10" r="1.3" fill="#e1141d"/><circle cx="16" cy="10" r="1.3" fill="#e1141d"/></svg>
</div>

</body>
</html>
```